Business card logo

Hello, I would like a business card for my law firm with a logo composed of my initials "MH". The logo is intended to appear on my business card, my letterhead, envelope and documents from my office. My first and last name (Maren Holt) and "Lawyer" must appear next to the logo. I would like the logo and the characters to be in golden color on a dark background (example black, navy blue). I would especially like a refined work on the logo which should be composed of the letters J and R.

```html
<!DOCTYPE html>
<html lang="en">
<head>
<meta charset="utf-8">
<title>Maren Holt, Lawyer – Business Card</title>
<link href="https://fonts.googleapis.com/css2?family=Arimo:wght@400;700&display=swap" rel="stylesheet">
<style>
  :root {
    --backdrop: #2a2a2b;
    --card: #1b1b1d;
    --card-pattern: #202023;
    --gold: #f6b318;
    --text-light: #d6d6d6;
    --text-muted: #9a9a9a;
    --divider: #4a4a4a;
  }
  * { box-sizing: border-box; margin: 0; padding: 0; }
  html, body {
    width: 1200px; height: 782px; overflow: hidden;
    background: var(--backdrop);
    font-family: "Arimo", Arial, sans-serif;
  }
  .stage {
    width: 1200px; height: 782px;
    display: flex; align-items: center; justify-content: center; gap: 50px;
  }
  .card {
    width: 525px; height: 300px;
    background: var(--card);
    position: relative;
    box-shadow: 0 14px 30px rgba(0,0,0,.45);
  }
  /* Front */
  .card--front { display: flex; }
  .identity {
    width: 50%;
    display: flex; flex-direction: column; align-items: center; justify-content: center;
  }
  .identity__mark {
    color: var(--gold); font-weight: 700; font-size: 46px; letter-spacing: 2px; line-height: 1;
    margin-bottom: 14px;
  }
  .identity__name {
    color: var(--gold); font-size: 28px; font-weight: 400; line-height: 1;
  }
  .identity__role {
    display: flex; align-items: center; gap: 8px; margin-top: 6px;
    color: var(--text-muted); font-size: 8px; letter-spacing: 7px;
  }
  .identity__role::before, .identity__role::after {
    content: ""; width: 34px; height: 1px; background: var(--gold);
  }
  .divider {
    position: absolute; left: 50%; top: 40px; bottom: 40px; width: 1px;
    background: linear-gradient(var(--card), var(--divider), var(--card));
  }
  .contact {
    width: 50%; padding: 0 0 0 30px;
    display: flex; flex-direction: column; justify-content: center;
  }
  .contact__name { color: var(--gold); font-size: 20px; line-height: 1.1; }
  .contact__title { color: var(--text-light); font-size: 13px; margin-bottom: 8px; }
  .contact__list { list-style: none; }
  .contact__item {
    display: flex; align-items: center; gap: 8px;
    color: var(--text-light); font-size: 13px; line-height: 1.45;
  }
  .contact__item svg { width: 10px; height: 10px; flex: none; fill: var(--gold); }
  .contact__address { color: var(--text-light); font-size: 13px; line-height: 1.35; margin-top: 4px; }
  /* Back */
  .card--back { display: flex; align-items: center; justify-content: center; overflow: hidden; }
  .back__pattern { position: absolute; inset: 0; background: var(--card-pattern); }
  .back__mark {
    position: relative; color: var(--gold); font-weight: 700; font-size: 38px; letter-spacing: 2px;
  }
</style>
</head>
<body>
<main class="stage">
  <section class="card card--front">
    <div class="identity">
      <div class="identity__mark">MH</div>
      <div class="identity__name">Maren Holt</div>
      <div class="identity__role">LAWYER</div>
    </div>
    <div class="divider"></div>
    <div class="contact">
      <div class="contact__name">Daniel Price</div>
      <div class="contact__title">Managing Director</div>
      <ul class="contact__list">
        <li class="contact__item">
          <svg viewBox="0 0 10 10"><path d="M1 3c0-1 1-2 2-2h4c1 0 2 1 2 2v1H7V3H3v1H1z M2 5h6l1 4H1z"/></svg>
          044-555 210 347
        </li>
        <li class="contact__item">
          <svg viewBox="0 0 10 10"><path d="M2.5 0h5v10h-5z M3.5 1v7h3V1z"/></svg>
          044-555 210 348
        </li>
        <li class="contact__item">
          <svg viewBox="0 0 10 10"><path d="M0 2h10v6H0z M0.8 2.6 5 5.6 9.2 2.6" stroke="#1b1b1d" stroke-width=".8"/></svg>
          office@holtlaw.example
        </li>
        <li class="contact__item">
          <svg viewBox="0 0 10 10"><circle cx="5" cy="5" r="5"/></svg>
          www.holtlaw.example
        </li>
      </ul>
      <div class="contact__address">48 Linden Row, Suite 3<br>Westbrook, 402157.</div>
    </div>
  </section>

  <section class="card card--back">
    <div class="back__pattern" role="img" aria-label="Faint repeating monogram pattern across the card back"></div>
    <div class="back__mark">MH</div>
  </section>
</main>
</body>
</html>
```